Flyer-Design für psychologische Beratungspraxis für Mütter
Zielgruppe
Gelassenheitswerkstatt ist eine psychologische Beratungspraxis. Ich unterstütze Mütter, Schwangere und Frauen mit Kinderwunsch bei Herausforderungen rund um Schwangerschaft, Geburt, Mutterschaft, und damit einhergehenden Problemen.
Aufgabenstellung
Text nochmal geringgradig geändert...siehe Datei anbei

```html
<!DOCTYPE html>
<html lang="de">
<head>
<meta charset="utf-8">
<title>Gelassenheitswerkstatt – Flyer</title>
<link href="https://fonts.googleapis.com/css2?family=Lora:ital@1&family=Poppins:wght@600;700&family=Quicksand:wght@400;500&family=Libre+Baskerville&display=swap" rel="stylesheet">
<style>
  :root {
    --paper: #fefefe;
    --ink: #111111;
    --brand-blue: #2e2a8c;
    --brand-green: #72b13c;
    --photo-light: #dcdcdc;
    --photo-dark: #8a8a8a;
  }
  html, body { margin: 0; padding: 0; overflow: hidden; }
  body { width: 848px; height: 1200px; background: var(--paper); position: relative; overflow: hidden; }
  .brand { position: absolute; left: 46px; top: 96px; display: flex; align-items: center; gap: 8px; }
  .brand-mark { width: 14px; height: 14px; border-radius: 50%; background: var(--brand-green); }
  .brand-name { font-family: "Quicksand", sans-serif; font-weight: 500; font-size: 14px; color: var(--brand-blue); letter-spacing: 0.5px; }
  .tagline { position: absolute; left: 145px; top: 187px; font-family: "Libre Baskerville", serif; font-size: 10.5px; letter-spacing: 2.6px; color: var(--ink); margin: 0; }
  .headline { position: absolute; left: 140px; top: 232px; margin: 0; font-family: "Poppins", sans-serif; font-weight: 700; font-size: 16.5px; line-height: 20px; color: var(--ink); letter-spacing: -0.2px; }
  .lead { position: absolute; left: 140px; top: 296px; width: 420px; margin: 0; font-family: "Lora", serif; font-style: italic; font-size: 17px; line-height: 20.5px; letter-spacing: 0.6px; color: var(--ink); }
  .question { position: absolute; left: 140px; top: 414px; margin: 0; font-family: "Poppins", sans-serif; font-weight: 700; font-size: 21px; letter-spacing: 2.3px; color: var(--ink); }
  .body-copy { position: absolute; left: 140px; top: 470px; width: 460px; margin: 0; font-family: "Quicksand", sans-serif; font-size: 14.3px; line-height: 20.2px; letter-spacing: 0.9px; color: var(--ink); }
  .photo-band { position: absolute; left: 0; top: 795px; width: 848px; height: 405px; background: linear-gradient(90deg, var(--photo-dark) 0%, var(--photo-light) 35%, #eeeeee 60%, var(--photo-dark) 100%); }
  .accent { position: absolute; left: 0; top: 0; }
</style>
</head>
<body>
  <div class="brand">
    <span class="brand-mark"></span>
    <span class="brand-name">Gelassenheitswerkstatt</span>
  </div>

  <p class="tagline">KRISENBEGLEITUNG UND LEBENSBERATUNG</p>

  <h1 class="headline">PSYCHOLOGISCHE BERATUNGSPRAXIS<br>FÜR MÜTTER, SCHWANGERE UND FRAUEN MIT KINDERWUNSCH</h1>

  <p class="lead">Mutter sein ist wunderbar. Wenn eine Frau Mutter wird, ist sie plötzlich verliebt über beide Ohren, unbändig stolz und von Glücksgefühlen völlig überwältigt.</p>

  <h2 class="question">SO IST ES DOCH „NORMAL“, ODER...?</h2>

  <p class="body-copy">Überforderung, Frustration und Verzweiflung kennen Mütter, Frauen mit Kinderwunsch und werdende Mütter allerdings ebenfalls nur zu gut. Wichtig ist, dass die Beurteilung einer Situation, d.h. wie stark sie uns belastet,allein uns selbst zusteht. Nur unsere eigene subjektive Einschätzung ist ausschlaggebend.<br>So unterschiedlich wir Menschen sind, so verschieden ist auch unser persönliches Fühlen und Erleben. Für unsere Herausforderungen benötigen wir deshalb individuell passende Lösungen.<br>Ja, Mutter sein ist wundervoll! Und ja, die Dynamik der Paarbeziehung verändert sich schlagartig und wir stehen plötzlich vor einer der erfüllendsten Aufgaben und zugleich einer der größten existentiellen Herausforderungen, die uns das Leben bietet: Eltern sein.</p>

  <div class="photo-band" role="img" aria-label="Schwarzweißfoto: links eine nachdenkliche Frau mit aufgestützten Armen, rechts der Bauch einer Schwangeren"></div>

  <svg class="accent" width="848" height="1200" viewBox="0 0 848 1200" aria-hidden="true">
    <polygon points="225,1200 848,1050 848,1200" fill="var(--brand-green)"/>
  </svg>
</body>
</html>
```